New Business card with our new logo

NEW BUSINESS CARDS wth our new logo

Want a sophisticated look. Probably in deep purple ink. (but we are open)
Would like something that looks expensive. Do not want a cutsie food look.
Not sure what more information I can offer. If you have any please contact me.

NAME - Ruth Delacroix Hale, Owner
415-273 0918
ruth@velvetplatterco.example
velvetplatterco.example

Target Market(s)

not sure what your are asking?

Industry/Entity Type

Business

Contact Information for Business Card

Logo + informaiton
Want a sophisticated look if possible. The cards are for women

Font styles to use
Serif

Colors
886aae

Requirements
Must have
• Ruth Delacroix Hale, Owner
• 415-273 0918
• ruth@velvetplatterco.example
• velvetplatterco.example
Nice to have
• suprise me
Should not have
• No cute food images, chef hat, knives, forks, etc.

```html
<!DOCTYPE html>
<html lang="en">
<head>
<meta charset="utf-8">
<title>Velvet Platter Co. — Business Card</title>
<link rel="stylesheet" href="https://fonts.googleapis.com/css2?family=Bodoni+Moda:wght@600&family=Questrial&display=swap">
<style>
  :root {
    --ink: #000000;
    --paper: #ffffff;
    --plum: #5f3c79;
    --lilac: #886aae;
    --lilac-shade: #71568f;
  }
  html, body {
    margin: 0;
    padding: 0;
    width: 687px;
    height: 1200px;
    overflow: hidden;
    background: var(--paper);
  }
  .card {
    position: relative;
    width: 687px;
    height: 1200px;
    background: var(--paper);
    font-family: "Questrial", sans-serif;
    color: var(--ink);
  }
  .card-shapes {
    position: absolute;
    inset: 0;
  }
  .brand {
    position: absolute;
    left: 80px;
    top: 210px;
    margin: 0;
    font-family: "Questrial", sans-serif;
    font-weight: 400;
    font-size: 50px;
    line-height: 1;
    letter-spacing: 1px;
    color: var(--plum);
    white-space: nowrap;
  }
  .person {
    position: absolute;
    left: 80px;
    top: 466px;
  }
  .person-name {
    margin: 0;
    font-family: "Bodoni Moda", serif;
    font-weight: 600;
    font-size: 43px;
    line-height: 1.1;
    letter-spacing: 0.5px;
    white-space: nowrap;
  }
  .person-role {
    margin: 2px 0 0;
    font-family: "Questrial", sans-serif;
    font-size: 52px;
    line-height: 1.1;
  }
  .contact-list {
    position: absolute;
    left: 80px;
    top: 782px;
    margin: 0;
    padding: 0;
    list-style: none;
  }
  .contact-item {
    display: flex;
    align-items: center;
    height: 62px;
    margin-bottom: 46px;
    font-size: 33px;
    white-space: nowrap;
  }
  .contact-icon {
    width: 52px;
    height: 56px;
    margin-right: 22px;
    flex: none;
  }
</style>
</head>
<body>
  <main class="card">
    <svg class="card-shapes" width="687" height="1200" viewBox="0 0 687 1200" aria-hidden="true">
      <rect class="card-frame" x="2" y="64" width="678" height="1127" fill="none" stroke="var(--ink)" stroke-width="3"/>
      <polygon class="ribbon-back" points="469,658 676,625 681,757" fill="var(--lilac)"/>
      <polygon class="ribbon-fold" points="469,658 681,757 469,746" fill="var(--lilac-shade)"/>
      <polygon class="ribbon-band" points="3,717 681,757 681,1100 3,1188" fill="var(--lilac)"/>
    </svg>

    <p class="brand">VELVET PLATTER CO.</p>

    <section class="person">
      <h1 class="person-name">Ruth Delacroix Hale</h1>
      <p class="person-role">Owner</p>
    </section>

    <ul class="contact-list">
      <li class="contact-item">
        <svg class="contact-icon" viewBox="0 0 52 56" aria-hidden="true">
          <path d="M10 4 L18 2 L22 16 L16 20 Q18 32 28 42 L34 36 L46 44 L42 52 Q34 58 20 44 Q4 26 10 4 Z" fill="var(--ink)"/>
        </svg>
        <span>415-273 0918</span>
      </li>
      <li class="contact-item">
        <svg class="contact-icon" viewBox="0 0 52 56" aria-hidden="true">
          <circle cx="26" cy="28" r="22" fill="none" stroke="var(--ink)" stroke-width="5"/>
          <circle cx="25" cy="28" r="9" fill="none" stroke="var(--ink)" stroke-width="5"/>
          <path d="M34 19 V36 Q36 42 44 38" fill="none" stroke="var(--ink)" stroke-width="5"/>
        </svg>
        <span>ruth@velvetplatterco.example</span>
      </li>
      <li class="contact-item">
        <svg class="contact-icon" viewBox="0 0 52 56" aria-hidden="true">
          <g fill="none" stroke="var(--ink)" stroke-width="2.5">
            <circle cx="26" cy="28" r="23"/>
            <ellipse cx="26" cy="28" rx="10" ry="23"/>
            <line x1="26" y1="5" x2="26" y2="51"/>
            <line x1="3" y1="28" x2="49" y2="28"/>
            <path d="M7 16 H45 M7 40 H45"/>
          </g>
        </svg>
        <span>velvetplatterco.example</span>
      </li>
    </ul>
  </main>
</body>
</html>
```